KT Crewing business card

Require business card which includes:
Company name: KT CREWING PTY LTD
Email: Mick@ktcrewing.com.au
Phone: 0431 556 208
ACN: 517 238 649

slogan: Onsite Auto Electrician Labour hire

Details and logo on top side
Logo only on bottom side

colour codes : #F15A29 , #939598

Target Market(s)

Western Australia mining sector

Industry/Entity Type

Mining

Contact Information for Business Card

Require business card which includes: Company name: KT CREWING PTY LTD Email: Mick@ktcrewing.com.au Phone: 0431 556 208 ACN: 517 238 649 slogan: Onsite Auto Electrician Labour hire Details and logo on top side Logo only on bottom side colour codes : #F15A29 , #939598

Colors
EE7325
F08F49
F5BC92
FAE3D3
FDF4ED

Requirements
Must have
• double sided

```html
<!DOCTYPE html>
<html lang="en">
<head>
<meta charset="utf-8">
<title>KT Crewing business card</title>
<link href="https://fonts.googleapis.com/css2?family=Poppins:wght@400;500&family=Rajdhani:wght@600;700&display=swap" rel="stylesheet">
<style>
  :root {
    --brand-orange: #F15A29;
    --brand-orange-soft: #F26736;
    --brand-grey: #939598;
    --text-grey: #6d6e71;
    --rule-grey: #cfd0d2;
    --ghost-grey: #e8e8e9;
    --card-white: #ffffff;
    --stage: #5e4a37;
  }
  * { margin: 0; padding: 0; box-sizing: border-box; }
  html, body { width: 900px; height: 1200px; overflow: hidden; }
  body {
    background: var(--stage);
    position: relative;
    font-family: "Poppins", Arial, sans-serif;
  }
  .card {
    position: absolute;
    left: 82px;
    width: 736px;
    height: 432px;
    border-radius: 30px;
    overflow: hidden;
    box-shadow: 0 6px 14px rgba(0,0,0,0.35);
  }
  .card-front { top: 128px; background: var(--card-white); }
  .card-back { top: 632px; background: var(--brand-orange); }

  .brand-name {
    position: absolute;
    font-family: "Rajdhani", Arial, sans-serif;
    font-weight: 700;
    white-space: nowrap;
    line-height: 1;
  }
  .front-brand { left: 40px; top: 70px; font-size: 66px; color: var(--brand-orange); }
  .front-brand-ghost { left: 358px; top: 66px; font-size: 84px; color: var(--ghost-grey); }

  .holder {
    position: absolute;
    left: 40px;
    top: 248px;
    display: flex;
    align-items: baseline;
    gap: 14px;
  }
  .holder-name {
    font-family: "Rajdhani", Arial, sans-serif;
    font-weight: 700;
    font-size: 31px;
    letter-spacing: 0.5px;
    color: var(--brand-orange);
  }
  .holder-role { font-size: 16px; color: var(--text-grey); }

  .rule {
    position: absolute;
    left: 40px;
    top: 286px;
    width: 658px;
    height: 1px;
    background: var(--rule-grey);
  }
  .contact-list {
    position: absolute;
    left: 40px;
    top: 298px;
    list-style: none;
  }
  .contact-item {
    display: flex;
    align-items: center;
    gap: 9px;
    font-size: 16px;
    color: var(--text-grey);
    height: 25px;
  }
  .contact-icon { width: 18px; height: 18px; flex: none; }
  .company-number {
    position: absolute;
    right: 38px;
    top: 298px;
    height: 25px;
    display: flex;
    align-items: center;
    font-size: 16px;
    color: var(--text-grey);
  }
  .company-number b { color: var(--brand-orange); font-weight: 500; margin-right: 4px; }

  .slogan-band {
    position: absolute;
    left: 0;
    bottom: 0;
    width: 100%;
    height: 50px;
    background: var(--brand-grey);
    color: var(--card-white);
    font-family: "Rajdhani", Arial, sans-serif;
    font-weight: 600;
    font-size: 19px;
    letter-spacing: 0.6px;
    display: flex;
    align-items: center;
    justify-content: center;
  }

  .back-pattern-area {
    position: absolute;
    inset: 0;
    background: linear-gradient(180deg, var(--brand-orange-soft), var(--brand-orange));
  }
  .back-brand {
    left: 0;
    right: 0;
    top: 178px;
    text-align: center;
    font-size: 82px;
    color: var(--card-white);
  }
</style>
</head>
<body>

<section class="card card-front" aria-label="Business card front">
  <div class="brand-name front-brand">KT Crewing</div>
  <div class="brand-name front-brand-ghost" aria-hidden="true">KT Crewing</div>

  <div class="holder">
    <span class="holder-name">MICK HOLLAND</span>
    <span class="holder-role">Managing Director</span>
  </div>
  <div class="rule"></div>

  <ul class="contact-list">
    <li class="contact-item">
      <svg class="contact-icon" viewBox="0 0 18 18" aria-hidden="true">
        <rect width="18" height="18" rx="2" fill="#F15A29"/>
        <path d="M5.2 4.2l2 0 .9 2.4-1.2.9a7 7 0 0 0 3.6 3.6l.9-1.2 2.4.9 0 2a1 1 0 0 1-1 1A9 9 0 0 1 4.2 5.2a1 1 0 0 1 1-1z" fill="#fff"/>
      </svg>
      0431 556 208
    </li>
    <li class="contact-item">
      <svg class="contact-icon" viewBox="0 0 18 18" aria-hidden="true">
        <rect width="18" height="18" rx="2" fill="#F15A29"/>
        <rect x="3.5" y="5" width="11" height="8" fill="none" stroke="#fff" stroke-width="1.4"/>
        <path d="M3.5 5l5.5 4.5L14.5 5" fill="none" stroke="#fff" stroke-width="1.4"/>
      </svg>
      Mick@ktcrewing.com.au
    </li>
  </ul>

  <div class="company-number"><b>ACN</b>: 517 238 649</div>

  <div class="slogan-band">Onsite Auto Electrician Labour hire</div>
</section>

<section class="card card-back" aria-label="Business card back">
  <div class="back-pattern-area" role="img" aria-label="Repeated faint brand pattern on orange background"></div>
  <div class="brand-name back-brand">KT Crewing</div>
</section>

</body>
</html>
```